Quillby Housecrafters Door Hanger design, Postcard and presentation folders Design

we are a home improvement company in Portland Oregon, are main service is roofing but we also do gutters, painting and pressure washing. we are a certified roofing contractor for TRV. We have over 20years of experince in the roofing industry we use top quality materials. Our mission is to do quality work and provide the best service.
Updates

This door hangers are going to be share to homeowners where we are currently working at! I will like to have a square maybe 2 inch wide and 1 inch hide (blank) for me to put the address where we are working at. So we want to give a direct message to homeowners who we are and why we are there for. Our services are roofing, gutters, painting, and pressure washing. But 95% of the door hangers should give the message that we are a roofing contractor. We are also certified by TRV which means all of our new roof projects have a 50 year warranty which only 2% of roofing contractor can offer that. We also offer finance, and all quality work. I will like to add photos of our trucks since all of them are wrap which will build them trust.

Target Market(s)

This door hangers should be custom for Homeowners with residential Homes,,, Average customer are between 40 & 65 Years old.

Industry/Entity Type

Roofing

Contact Information for Business Card

Logo, name, phone number, credentials, and services like roofing gutters painting and pressure washing

Font styles to use
Serif
Sans Serif
Decorative

Colors
33b8a4
5c5c5c

Requirements
Must have
• I want tho have a folder design just like this business card sample i uploaded. Teal and charcoal with services ...
Nice to have
• company trucks, job photo, crew photo and credential photos
Should not have
• I dont want it too busy or crowded..

```html
<!DOCTYPE html>
<html lang="en">
<head>
<meta charset="utf-8">
<title>Quillby Housecrafters Door Hanger</title>
<link href="https://fonts.googleapis.com/css2?family=Bebas+Neue&family=Poppins:wght@400;500;600;700&display=swap" rel="stylesheet">
<style>
  :root{
    --teal-deep:#13675f;
    --teal-dark:#0f4f49;
    --teal-bright:#1d9a88;
    --charcoal:#5c5c5c;
    --white:#ffffff;
    --badge-red:#d8282f;
    --line-grey:#c9c9c9;
  }
  html,body{margin:0;padding:0;overflow:hidden;}
  body{width:1200px;height:1200px;background:var(--white);position:relative;font-family:"Poppins",sans-serif;}
  .hanger{position:absolute;top:54px;width:423px;height:1093px;overflow:hidden;box-shadow:2px 3px 8px rgba(0,0,0,.25);background:var(--white);}
  .hanger--front{left:127px;}
  .hanger--back{left:650px;}
  .shingle-band{position:absolute;left:0;top:0;width:100%;height:246px;
    background:linear-gradient(160deg,#0e4a44 0%,#1b6d64 35%,#0d433e 55%,#1e7a70 80%,#124f49 100%);}
  .hanger-hole{position:absolute;top:41px;width:174px;height:174px;border-radius:50%;background:var(--white);}
  .hanger-slot{position:absolute;top:117px;height:22px;background:var(--white);}
  .front .hanger-hole{left:124px;}
  /* front */
  .brand-block{position:absolute;top:246px;left:0;width:100%;height:283px;background:var(--white);text-align:center;}
  .brand-mark{position:absolute;left:50%;top:84px;transform:translateX(-50%);width:40px;height:40px;background:var(--teal-bright);}
  .brand-name{position:absolute;top:142px;width:100%;font-family:"Poppins",sans-serif;font-weight:600;font-size:28px;line-height:36px;color:var(--teal-bright);}
  .hero{position:absolute;top:529px;left:0;width:100%;height:564px;
    background:linear-gradient(180deg,#13675f 0%,#2a6a63 30%,#4a6e68 55%,#7d7d72 75%,#8a8878 100%);}
  .hero-text{background:none;}
  .hero-headline{position:absolute;top:54px;width:100%;margin:0;text-align:center;font-family:"Bebas Neue",sans-serif;font-weight:400;font-size:48px;line-height:44px;color:var(--white);letter-spacing:.5px;}
  .hero-headline .dot{color:var(--teal-bright);}
  .hero-sub{position:absolute;top:171px;width:100%;margin:0;text-align:center;font-weight:600;font-size:13px;color:var(--white);}
  .hero-rule{position:absolute;top:207px;left:127px;width:168px;height:1px;background:rgba(255,255,255,.7);}
  .social-row{position:absolute;top:228px;left:0;width:100%;display:flex;justify-content:center;gap:46px;}
  .social-dot{width:24px;height:24px;border:2px solid var(--white);border-radius:50%;box-sizing:border-box;}
  .address-box{position:absolute;top:902px;left:40px;width:339px;height:115px;background:var(--white);border-radius:6px;}
  .address-line{position:absolute;left:19px;width:300px;height:1px;background:var(--line-grey);}
  /* back */
  .url-band{position:absolute;top:246px;left:0;width:100%;height:55px;background:var(--teal-deep);color:var(--white);text-align:center;font-weight:700;font-size:21px;line-height:55px;}
  .cert-strip{position:absolute;top:301px;left:0;width:100%;height:56px;background:var(--white);display:flex;align-items:center;justify-content:center;gap:18px;}
  .cert-text{color:var(--teal-deep);font-weight:600;font-size:12.5px;}
  .cert-badge{width:70px;height:20px;background:var(--badge-red);border-radius:2px;}
  .services{position:absolute;top:357px;left:0;width:100%;height:273px;
    background:linear-gradient(165deg,#1a6e66 0%,#13675f 40%,#0f5650 70%,#1a6a62 100%);color:var(--white);}
  .section-title{margin:0;font-family:"Bebas Neue",sans-serif;font-weight:400;font-size:37px;line-height:1;color:var(--white);}
  .section-title .dot{color:var(--teal-bright);}
  .services .section-title{position:absolute;top:33px;width:100%;text-align:center;}
  .service-list{position:absolute;top:80px;left:42px;width:360px;display:grid;grid-template-columns:158px 1fr;row-gap:19px;margin:0;padding:0;list-style:none;}
  .service-item{display:flex;align-items:center;gap:10px;font-weight:500;font-size:13.5px;height:21px;}
  .service-item--main{font-weight:600;font-size:17px;}
  .tick{width:20px;height:16px;flex:none;}
  .services-rule{position:absolute;top:203px;left:26px;width:370px;height:1px;background:rgba(255,255,255,.8);}
  .values{position:absolute;top:222px;left:20px;width:383px;margin:0;text-align:center;font-size:10px;line-height:13px;}
  .contact{position:absolute;top:630px;left:0;width:100%;height:218px;background:var(--teal-deep);color:var(--white);}
  .contact .section-title{position:absolute;top:12px;left:117px;}
  .tag{position:absolute;}
  .contact-address{position:absolute;top:48px;left:119px;font-weight:600;font-size:15px;line-height:20px;}
  .contact-email{position:absolute;top:119px;left:119px;font-weight:600;font-size:15px;}
  .contact-phone{position:absolute;top:156px;left:118px;font-family:"Bebas Neue",sans-serif;font-size:50px;line-height:1;letter-spacing:.5px;}
  .truck-photo{position:absolute;top:848px;left:0;width:100%;height:245px;
    background:linear-gradient(180deg,#7a6a58 0%,#4c4e48 35%,#9aa5a8 60%,#3e4240 100%);}
</style>
</head>
<body>

<section class="hanger hanger--front front">
  <div class="shingle-band" role="img" aria-label="Close-up photo of roof shingles tinted teal"></div>
  <div class="hanger-slot" style="left:0;width:140px;"></div>
  <div class="hanger-hole"></div>

  <div class="brand-block">
    <div class="brand-mark"></div>
    <div class="brand-name">Quillby Housecrafters</div>
  </div>

  <div class="hero" role="img" aria-label="Photo of a house with a new grey shingle roof and beige siding, tinted teal at the top"></div>
  <div class="hero hero-text">
    <h1 class="hero-headline">PORTLAND'S TOP-RATED<br>ROOFING COMPANY<span class="dot">.</span></h1>
    <p class="hero-sub">Let Our Experts Help With Your Next Home Project.</p>
    <div class="hero-rule"></div>
    <div class="social-row" aria-label="Social media">
      <span class="social-dot"></span><span class="social-dot"></span><span class="social-dot"></span>
    </div>
  </div>

  <div class="address-box" aria-label="Blank space for job site address">
    <div class="address-line" style="top:40px;"></div>
    <div class="address-line" style="top:79px;"></div>
  </div>
</section>

<section class="hanger hanger--back">
  <div class="shingle-band" role="img" aria-label="Close-up photo of roof shingles tinted teal"></div>
  <div class="hanger-slot" style="left:290px;width:133px;"></div>
  <div class="hanger-hole" style="left:123px;"></div>

  <div class="url-band">quillbyhousecrafters.com</div>
  <div class="cert-strip">
    <span class="cert-text">OUR COMPANY IS TRV CERTIFIED.</span>
    <span class="cert-badge" role="img" aria-label="Certification badge"></span>
  </div>

  <div class="services">
    <h2 class="section-title">OUR SERVICES<span class="dot">.</span></h2>
    <ul class="service-list">
      <li class="service-item service-item--main"><svg class="tick" viewBox="0 0 20 16"><path d="M2 8l5 5L18 2" fill="none" stroke="#fff" stroke-width="3.5"/></svg>ROOFING</li>
      <li class="service-item"><svg class="tick" viewBox="0 0 20 16"><path d="M2 8l5 5L18 2" fill="none" stroke="#fff" stroke-width="3.5"/></svg>SIDING</li>
      <li class="service-item"><svg class="tick" viewBox="0 0 20 16"><path d="M2 8l5 5L18 2" fill="none" stroke="#fff" stroke-width="3.5"/></svg>GUTTERS</li>
      <li class="service-item"><svg class="tick" viewBox="0 0 20 16"><path d="M2 8l5 5L18 2" fill="none" stroke="#fff" stroke-width="3.5"/></svg>PRESSURE WASHING</li>
      <li class="service-item"><svg class="tick" viewBox="0 0 20 16"><path d="M2 8l5 5L18 2" fill="none" stroke="#fff" stroke-width="3.5"/></svg>PAINTING</li>
      <li class="service-item"><svg class="tick" viewBox="0 0 20 16"><path d="M2 8l5 5L18 2" fill="none" stroke="#fff" stroke-width="3.5"/></svg>ATTIC VENTILATON</li>
    </ul>
    <div class="services-rule"></div>
    <p class="values">FAMILY OWNED | NO SALES PITCH | NO SUB-CONTRACTING | NO<br>PROJECT LEFT BEHIND | WE OFFER FINANCE | QUALITY WORK</p>
  </div>

  <div class="contact">
    <h2 class="section-title">CONTACT<span class="dot">.</span></h2>
    <svg class="tag" style="left:62px;top:48px;" width="31" height="20" viewBox="0 0 31 20">
      <path d="M0 0h24l7 10-7 10H0z" fill="#8d8d8d"/>
      <path d="M14 15s-4-4-4-7a4 4 0 018 0c0 3-4 7-4 7z" fill="none" stroke="#fff" stroke-width="1.3"/>
      <circle cx="14" cy="8" r="1.3" fill="#fff"/>
    </svg>
    <div class="contact-address">Portland,<br>OR 97201,<br>United States</div>
    <svg class="tag" style="left:62px;top:119px;" width="31" height="20" viewBox="0 0 31 20">
      <path d="M0 0h24l7 10-7 10H0z" fill="#8d8d8d"/>
      <rect x="9" y="6" width="11" height="8" fill="none" stroke="#fff" stroke-width="1.3"/>
      <path d="M9 6l5.5 4.5L20 6" fill="none" stroke="#fff" stroke-width="1.3"/>
    </svg>
    <div class="contact-email">hello@quillbyhousecrafters.com</div>
    <svg class="tag" style="left:34px;top:165px;" width="58" height="35" viewBox="0 0 58 35">
      <path d="M0 0h45l13 17.5L45 35H0z" fill="#8d8d8d"/>
      <path d="M24 9c-3 0-4 3-3 7s4 9 8 10c2 1 4 0 4-2l-3-3-2 1c-2-1-3-3-3-5l2-1-1-4z" fill="#fff"/>
    </svg>
    <div class="contact-phone">(503)555-0142</div>
  </div>

  <div class="truck-photo" role="img" aria-label="Photo of the company's wrapped pickup truck parked outside a home"></div>
</section>

</body>
</html>
```